KRV Business Cards

We are a local commercial development company based in Silicon Valley and we would like a new business card. I've attached a copy of our company brochure to give a flavor of what we do, our logo, info company colors/graphics, and our current business card. We don't necessarily need a crazy makeover, but would like something that feels a little bit more "fresh" and modern (we've had the same business card design for 15+ years), but still in keeping with our overall brand -- clean, high-quality, modern but timeless. Would like to add our website to the info on the card (www.velmara.com) and would like the flexibility for some folks to have an efax number listed and some not to have that included (without it looking like there is a hole).

```html
<!DOCTYPE html>
<html lang="en">
<head>
<meta charset="utf-8">
<title>KRV Business Cards</title>
<link rel="stylesheet" href="https://fonts.googleapis.com/css2?family=Cinzel:wght@400&family=Open+Sans:wght@400;600&display=swap">
<style>
  :root {
    --backdrop: #e6e8eb;
    --paper: #f7f7f6;
    --navy: #34506e;
    --ink: #3a3d42;
    --rule: #d4d6d9;
    --back-top: #5b88b3;
    --back-bottom: #2e5275;
    --on-navy: #eef2f6;
  }
  * { margin: 0; padding: 0; box-sizing: border-box; }
  html, body { width: 1200px; height: 844px; overflow: hidden; }
  body {
    background: var(--backdrop);
    position: relative;
    font-family: "Open Sans", Arial, sans-serif;
  }
  .card {
    position: absolute;
    top: 272px;
    width: 525px;
    height: 300px;
    box-shadow: 0 6px 18px rgba(0,0,0,0.18);
  }
  .card-front { left: 55px; background: var(--paper); }
  .card-back {
    left: 620px;
    background: linear-gradient(160deg, var(--back-top), var(--back-bottom));
  }

  .company-name {
    position: absolute;
    display: flex;
    align-items: center;
    gap: 10px;
    font-family: "Open Sans", Arial, sans-serif;
    font-weight: 600;
    line-height: 1.25;
  }
  .company-mark {
    flex: none;
    width: 14px;
    height: 14px;
  }
  .card-front .company-name {
    top: 52px; right: 28px;
    width: 226px;
    font-size: 15px;
    color: var(--navy);
  }
  .card-front .company-mark { background: var(--navy); }
  .card-back .company-name {
    top: 100px; left: 0; right: 0;
    justify-content: center;
    font-size: 17px;
    color: var(--on-navy);
  }
  .card-back .company-mark { background: var(--on-navy); }
  .tagline {
    position: absolute;
    top: 168px; left: 0; right: 0;
    text-align: center;
    font-size: 12px;
    line-height: 1.4;
    color: var(--on-navy);
  }

  .rule {
    position: absolute;
    left: 26px; right: 26px;
    height: 1px;
    background: var(--rule);
  }
  .rule-top { top: 150px; }
  .rule-mid { top: 228px; }

  .person {
    position: absolute;
    left: 28px; top: 158px;
  }
  .person-name {
    font-family: "Cinzel", "Times New Roman", serif;
    font-size: 22px;
    color: var(--navy);
    letter-spacing: 0.5px;
    line-height: 1.15;
  }
  .person-title {
    font-size: 13px;
    color: var(--ink);
  }
  .address {
    position: absolute;
    left: 28px; top: 203px;
    font-size: 13.5px;
    color: var(--ink);
  }
  .contact {
    position: absolute;
    left: 28px; top: 238px;
    font-size: 13.5px;
    color: var(--ink);
    line-height: 1.5;
  }
  .label, .web { color: var(--navy); font-weight: 600; }
  .sep { color: #9a9ea4; margin: 0 5px; }
</style>
</head>
<body>
  <section class="card card-front" aria-label="Business card front">
    <div class="company-name"><span class="company-mark"></span><span>Velmara Development Company, LLC</span></div>
    <div class="rule rule-top"></div>
    <div class="person">
      <div class="person-name">Dana L. Whitford</div>
      <div class="person-title">Partner</div>
    </div>
    <div class="address">218 Linden Street, Mountain View, California 94041</div>
    <div class="rule rule-mid"></div>
    <div class="contact">
      <div><span class="label">DIRECT:</span> 555.014.0738<span class="sep">|</span><span class="label">P:</span> 555.014.0777<span class="sep">|</span><span class="label">F:</span> 555.014.3323</div>
      <div><span class="label">E:</span> dana@velmara.com<span class="sep">|</span><span class="web">www.velmara.com</span></div>
    </div>
  </section>

  <section class="card card-back" aria-label="Business card back">
    <div class="company-name"><span class="company-mark"></span><span>Velmara Development Company, LLC</span></div>
    <div class="tagline">Excellence in<br>Commercial Development</div>
  </section>
</body>
</html>
```